IT Company Business Card Rebranding

We want to modernize our business cards massively. We want to incorporate aspects of our old business card such as the white and geometric design with the blues of another icon. Existing Logo, old business card and icon are all attached.

We are a modern IT company that provides support for new and growing technologies and want our business cards to be modern yet professional.
Updates

Note: Do not use file ICON.png in design. This is just a design we like Added Wednesday, March 9, 2016

Industry/Entity Type

Information Technology

Contact Information for Business Card

Roughly 43 : 26 or 1075 x 650 px

Font styles to use
Serif

Colors
0492cd
3276b5
33a6d7
86cfc6
cfeae6
cee9f5
ffffff

Requirements
Must have
• Modern yet professional
Nice to have
• We would like to incorporate the blues of our existing logo and of the icon provided. Really like the design of the icon.
Should not have
• Too Decorative. Just simple and professional.
• Not have the circle icon, as it is a copyrighted icon, I just like the colors and the geometric design

```html
<!DOCTYPE html>
<html lang="en">
<head>
<meta charset="utf-8">
<title>Business Card – Ben Carter</title>
<link rel="stylesheet" href="https://fonts.googleapis.com/css2?family=Open+Sans:wght@300;400;700&family=Oswald:wght@300&display=swap">
<style>
  :root {
    --bg-deep: #0a4f6e;
    --bg-mid: #0b5f83;
    --bg-light: #136d93;
    --ink: #ffffff;
    --ink-soft: #b9dcec;
  }
  * { margin: 0; padding: 0; box-sizing: border-box; }
  html, body { width: 1200px; height: 725px; overflow: hidden; background: var(--bg-deep); }
  .card {
    position: relative;
    width: 1200px;
    height: 725px;
    overflow: hidden;
  }
  .card-backdrop {
    position: absolute;
    inset: 0;
    background:
      radial-gradient(ellipse at 30% 20%, var(--bg-light) 0%, transparent 60%),
      linear-gradient(135deg, var(--bg-mid) 0%, var(--bg-deep) 100%);
  }
  .identity {
    position: absolute;
    left: 80px;
    top: 305px;
    color: var(--ink);
  }
  .identity-name {
    font-family: "Open Sans", sans-serif;
    font-size: 64px;
    line-height: 1;
    letter-spacing: 0;
    text-transform: uppercase;
  }
  .identity-name .first { font-weight: 300; }
  .identity-name .last { font-weight: 700; }
  .identity-role {
    margin-top: 10px;
    font-family: "Open Sans", sans-serif;
    font-weight: 400;
    font-size: 23px;
    color: var(--ink-soft);
    text-transform: uppercase;
    letter-spacing: 0.3px;
  }
  .contact-list {
    position: absolute;
    left: 666px;
    top: 245px;
    list-style: none;
  }
  .contact-item {
    display: flex;
    align-items: center;
    height: 68px;
  }
  .contact-icon {
    width: 44px;
    height: 44px;
    margin-right: 31px;
    fill: var(--ink);
  }
  .contact-text {
    font-family: "Oswald", sans-serif;
    font-weight: 300;
    font-size: 36px;
    color: var(--ink);
    letter-spacing: 0.3px;
  }
</style>
</head>
<body>
  <div class="card">
    <div class="card-backdrop" role="img" aria-label="Deep blue faceted geometric background"></div>

    <div class="identity">
      <h1 class="identity-name"><span class="first">Ben</span><span class="last">Carter</span></h1>
      <p class="identity-role">Director of Technical Services</p>
    </div>

    <ul class="contact-list">
      <li class="contact-item">
        <svg class="contact-icon" viewBox="0 0 24 24" aria-hidden="true">
          <path d="M6.6 10.8c1.4 2.8 3.8 5.1 6.6 6.6l2.2-2.2c.3-.3.7-.4 1-.2 1.1.4 2.3.6 3.6.6.6 0 1 .4 1 1V20c0 .6-.4 1-1 1C10.6 21 3 13.4 3 4c0-.6.4-1 1-1h3.5c.6 0 1 .4 1 1 0 1.3.2 2.5.6 3.6.1.3 0 .7-.2 1z"/>
        </svg>
        <span class="contact-text">+61 3 5550 0198</span>
      </li>
      <li class="contact-item">
        <svg class="contact-icon" viewBox="0 0 24 24" aria-hidden="true">
          <path d="M12 2C8.1 2 5 5.1 5 9c0 5.2 7 13 7 13s7-7.8 7-13c0-3.9-3.1-7-7-7zm0 9.5c-1.4 0-2.5-1.1-2.5-2.5S10.6 6.5 12 6.5s2.5 1.1 2.5 2.5-1.1 2.5-2.5 2.5z"/>
        </svg>
        <span class="contact-text">Ballarat, Victoria 3350</span>
      </li>
      <li class="contact-item">
        <svg class="contact-icon" viewBox="0 0 24 24" aria-hidden="true">
          <path d="M3 5h18v2.2l-9 5.6-9-5.6z"/>
          <path d="M3 9.4l9 5.6 9-5.6V19H3z"/>
        </svg>
        <span class="contact-text">contact@techforge.com.au</span>
      </li>
      <li class="contact-item">
        <svg class="contact-icon" viewBox="0 0 24 24" aria-hidden="true">
          <path d="M12 3a9 9 0 1 0 0 18 9 9 0 0 0 0-18zm-1 15.9A7 7 0 0 1 5.1 10.2L9 14v1c0 1.1.9 2 2 2zm6.9-2.5c-.3-.8-1-1.4-1.9-1.4h-1v-3c0-.6-.4-1-1-1H8v-2h2c.6 0 1-.4 1-1V6h2c1.1 0 2-.9 2-2v-.4a7 7 0 0 1 2.9 12.8z"/>
        </svg>
        <span class="contact-text">www.techforge.com.au</span>
      </li>
    </ul>
  </div>
</body>
</html>
```